Corvale Spine & Joint Business Card

Need a business card using the logo provided. I want brand side of the card to be grey with the logo in the center of the card in white.

On the other side I leave to the designers

Target Market(s)

Personal Injury Attorneys

Industry/Entity Type

Medical

Contact Information for Business Card

Name, CEO. Cell Phone, (Hialeah, Address, Phone) (Homestead, Address, Phone) (Tallahassee, Address, Phone)

Colors

Designer to choose only greyscale colors for use in the design.

Requirements
Must have
• Logo by itself on one side

```html
<!DOCTYPE html>
<html lang="en">
<head>
<meta charset="utf-8">
<title>Corvale Spine &amp; Joint Business Card</title>
<link href="https://fonts.googleapis.com/css2?family=Montserrat:wght@400;500;600&family=Lato:wght@700&display=swap" rel="stylesheet">
<style>
  :root {
    --backdrop: #9bb6be;
    --card-grey: #686c75;
    --card-white: #ffffff;
    --ink-dark: #1f1f22;
    --ink-body: #3a3a3e;
    --ink-logo: #2f2f33;
  }
  html, body {
    margin: 0;
    width: 1200px;
    height: 1000px;
    overflow: hidden;
    background: var(--backdrop);
  }
  .canvas {
    position: relative;
    width: 1200px;
    height: 1000px;
  }
  .card {
    position: absolute;
    top: 349px;
    width: 468px;
    height: 303px;
  }
  .card--brand {
    left: 100px;
    background: var(--card-grey);
    display: flex;
    align-items: center;
    justify-content: center;
  }
  .card--contact {
    left: 632px;
    background: var(--card-white);
    font-family: "Montserrat", sans-serif;
  }
  .wordmark {
    font-family: "Lato", sans-serif;
    font-weight: 700;
    text-align: center;
    line-height: 1;
  }
  .wordmark__name { display: block; letter-spacing: 0.12em; }
  .wordmark__sub { display: block; letter-spacing: 0.12em; }
  .card--brand .wordmark { color: var(--card-white); margin-top: 4px; }
  .card--brand .wordmark__name { font-size: 30px; }
  .card--brand .wordmark__sub { font-size: 15px; margin-top: 8px; }
  .card--contact .wordmark {
    position: absolute;
    top: 29px;
    right: 29px;
    color: var(--ink-logo);
  }
  .card--contact .wordmark__name { font-size: 17px; }
  .card--contact .wordmark__sub { font-size: 8.5px; margin-top: 4px; }
  .person {
    position: absolute;
    left: 29px;
    top: 139px;
  }
  .person__name {
    margin: 0;
    font-size: 22px;
    font-weight: 500;
    color: var(--ink-dark);
  }
  .person__role {
    margin: 4px 0 0;
    font-size: 15px;
    color: var(--ink-body);
  }
  .contact-lines, .address {
    position: absolute;
    top: 214px;
    margin: 0;
    font-size: 15px;
    line-height: 19px;
    color: var(--ink-body);
    font-style: normal;
  }
  .contact-lines { left: 29px; line-height: 24px; top: 211px; }
  .address { left: 291px; }
</style>
</head>
<body>
<main class="canvas">
  <section class="card card--brand" aria-label="Card front">
    <div class="wordmark">
      <span class="wordmark__name">CORVALE</span>
      <span class="wordmark__sub">SPINE &amp; JOINT</span>
    </div>
  </section>
  <section class="card card--contact" aria-label="Card back">
    <div class="wordmark">
      <span class="wordmark__name">CORVALE</span>
      <span class="wordmark__sub">SPINE &amp; JOINT</span>
    </div>
    <div class="person">
      <h1 class="person__name">Daniel Hartley</h1>
      <p class="person__role">Chief Executive Officer</p>
    </div>
    <p class="contact-lines">+1 555 0142 7788<br>corvalespineandjoint.com</p>
    <address class="address">412 Cedar Lane,<br>Harlow Springs.<br>Texas.</address>
  </section>
</main>
</body>
</html>
```